UI improvement for an existing app

Hi, we have a mobile preorder app that was built with standard flutter UI.

Looking at improving the whole look and feel of our app and make it look more slick and on trend. Something similar to fennoplate, Quorvalo or something along these lines.

Keeping in mind that we are white labeling our app so it needs to be easily redline for other clients.

For our first client I've attached their branding guideline in this project as well.

Please find all the existing screen of our app which we are looking to improve.

Main focus is to give the app a modern and fresh look while making it easy to realign. Do ensure user experience and how they navigate the app is important

Feel free to let me know if you have any questions.

Thanks
KT

Need extra days to review

• All the functionality layout on the screenshot. There's some element that we would like to incorporate such as

1. Coupon code in checkout screen
2. Allow users to edit their profile in profile page

```html
<!DOCTYPE html>
<html lang="en">
<head>
<meta charset="utf-8">
<title>Verdaleaf – Preorder App Screens</title>
<link rel="stylesheet" href="https://fonts.googleapis.com/css2?family=Mulish:wght@400;600;700;800&display=swap">
<style>
:root{
  --bg:#eef0f3;
  --screen:#fafbfc;
  --white:#ffffff;
  --green:#6db562;
  --green-dark:#2f8a2a;
  --green-mid:#8cc36f;
  --lime:#d6e49c;
  --lime-pale:#e9f0c8;
  --ink:#2d2d2d;
  --muted:#9a9ea6;
  --line:#d9dce1;
  --red:#ef3b3b;
  --gold:#f2c230;
  --placeholder:#dfe3d6;
  --shadow:0 18px 40px rgba(80,90,110,.14);
}
*{box-sizing:border-box;margin:0;padding:0}
html,body{width:1200px;height:2290px;overflow:hidden;background:var(--bg);font-family:'Mulish',sans-serif;color:var(--ink)}
.canvas{position:relative;width:1200px;height:2290px}
.screen{position:absolute;width:340px;height:736px;border-radius:42px;background:var(--screen);overflow:hidden;box-shadow:var(--shadow)}
.abs{position:absolute}
.brand{font-weight:800;color:var(--ink);letter-spacing:-.5px;display:flex;align-items:center;gap:8px}
.brand .dot{width:.55em;height:.55em;border-radius:50%;background:var(--green)}
.tagline{font-size:12px;color:var(--muted);font-weight:600}
.btn{position:absolute;border-radius:30px;display:flex;align-items:center;justify-content:center;font-weight:700;font-size:13px}
.btn-green{background:var(--green);color:var(--white);box-shadow:0 8px 16px rgba(109,181,98,.35)}
.btn-white{background:var(--white);color:var(--ink);box-shadow:0 8px 18px rgba(80,90,110,.12)}
.field{position:absolute;left:52px;width:236px;height:50px;border:1px solid var(--line);border-radius:4px}
.field span{position:absolute;top:-8px;left:22px;background:var(--screen);padding:0 6px;font-size:10px;font-weight:700}
.nav{position:absolute;left:18px;right:18px;bottom:18px;height:56px;background:var(--white);border-radius:28px;box-shadow:0 10px 24px rgba(80,90,110,.12);display:flex;justify-content:space-around;align-items:center}
.nav svg{width:20px;height:20px;fill:none;stroke:var(--ink);stroke-width:1.6;stroke-linecap:round;stroke-linejoin:round}
.nav .active svg{stroke:var(--green)}
.nav .active{position:relative}
.nav .active::after{content:"";position:absolute;left:-8px;right:-8px;bottom:-8px;height:2px;background:var(--green);border-radius:2px}
.product-photo{border-radius:6px;background:var(--placeholder)}
.on-green{background:rgba(255,255,255,.45)}
.option-box{border-radius:4px}
.photo{border-radius:6px}
.avatar{border-radius:50%;background:linear-gradient(135deg,#e9c7a8,#b58a6a);border:2px solid var(--white);box-shadow:0 4px 10px rgba(0,0,0,.12)}
.small{font-size:10px;font-weight:700}
.meta{font-size:8px;color:var(--muted);line-height:1.35}
.chip{display:inline-flex;align-items:center;justify-content:center;height:22px;padding:0 12px;border-radius:12px;border:1px solid var(--green);color:var(--green);font-size:10px;font-weight:700;margin-right:8px;background:var(--white)}
.chip.on{background:var(--green);color:var(--white)}
.round{position:absolute;border-radius:50%;display:flex;align-items:center;justify-content:center;color:var(--white);font-weight:800}
.side-label{position:absolute;left:8px;transform:rotate(-90deg);transform-origin:left top;font-size:9px;font-weight:800;white-space:nowrap}
</style>
</head>
<body>
<div class="canvas">

<!-- Welcome -->
<section class="screen" style="left:50px;top:330px" aria-label="Welcome screen">
  <div class="abs" style="left:0;right:0;top:190px;text-align:center">
    <div class="brand" style="font-size:40px;justify-content:center">Verdaleaf<span class="dot"></span></div>
    <div class="tagline" style="margin-top:4px">Stay fresh</div>
  </div>
  <div class="btn btn-green" style="left:64px;width:212px;height:40px;top:430px">Login</div>
  <div class="abs" style="left:18px;right:18px;top:503px;display:flex;align-items:center;gap:28px">
    <div style="flex:1;height:1px;background:var(--line)"></div><span class="small" style="font-size:9px">OR</span><div style="flex:1;height:1px;background:var(--line)"></div>
  </div>
  <div class="btn btn-white" style="left:48px;width:150px;height:40px;top:560px">Create an Account</div>
  <div class="btn btn-green" style="left:220px;width:56px;height:40px;top:560px"><span style="width:10px;height:10px;border-radius:50%;background:var(--white)"></span></div>
</section>

<!-- Login -->
<section class="screen" style="left:430px;top:330px" aria-label="Login screen">
  <div class="abs" style="left:0;right:0;top:86px;text-align:center">
    <div class="brand" style="font-size:36px;justify-content:center">Verdaleaf<span class="dot"></span></div>
    <div class="tagline" style="margin-top:4px">Stay fresh</div>
  </div>
  <div class="abs" style="left:52px;top:232px">
    <div style="font-size:18px;font-weight:800;color:var(--muted)">Welcome Back!</div>
    <div style="font-size:12px;font-weight:700;margin-top:2px">Mei Lun</div>
  </div>
  <div class="field" style="top:320px"><span>Email Address</span></div>
  <div class="field" style="top:388px"><span>Password</span></div>
  <div class="btn btn-white" style="left:52px;width:96px;height:34px;top:474px;font-size:10px">Reset Password</div>
  <div class="btn btn-green" style="left:200px;width:88px;height:34px;top:474px">Login</div>
  <p class="abs meta" style="left:40px;right:40px;top:610px;text-align:center;color:var(--ink);font-weight:600">By login you have agree to Terms of use and Privacy Policy on Verdaleaf.</p>
</section>

<!-- Home -->
<section class="screen" style="left:810px;top:330px" aria-label="Home screen">
  <div class="brand abs" style="left:118px;top:58px;font-size:20px">Verdaleaf<span class="dot"></span></div>
  <div class="abs avatar" role="img" aria-label="User profile photo" style="left:270px;top:50px;width:36px;height:36px"></div>
  <div class="abs" style="left:22px;right:22px;top:104px;height:38px;border-radius:19px;background:var(--white);box-shadow:0 6px 16px rgba(80,90,110,.1);display:flex;align-items:center;padding:0 16px;gap:12px">
    <svg width="14" height="14" viewBox="0 0 24 24" fill="none" stroke="var(--muted)" stroke-width="2"><circle cx="10" cy="10" r="7"/><path d="M15 15l6 6"/></svg>
    <span style="font-size:9px;font-style:italic;color:var(--muted);flex:1">Find Verdaleaf</span>
    <svg width="16" height="14" viewBox="0 0 24 20" fill="none" stroke="var(--green)" stroke-width="2" stroke-linecap="round"><path d="M2 5h20M2 15h20"/><circle cx="8" cy="5" r="2" fill="var(--white)"/><circle cx="16" cy="15" r="2" fill="var(--white)"/></svg>
  </div>
  <div class="abs photo" role="img" aria-label="Promotional banner for the Bunny Pop collaboration cup" style="left:24px;right:24px;top:162px;height:86px;background:linear-gradient(90deg,#f0d23a 0 45%,#8ccbd8 45% 100%)"></div>
  <div class="abs" style="left:24px;top:264px;font-size:12px;font-weight:800;color:var(--green-dark)">Near by Verdaleaf cafe</div>
  <div class="round" style="left:288px;top:256px;width:30px;height:30px;background:var(--lime-pale)"><svg width="16" height="16" viewBox="0 0 24 24" fill="none" stroke="var(--ink)" stroke-width="1.8" stroke-linejoin="round"><path d="M3 6l6-3 6 3 6-3v15l-6 3-6-3-6 3z"/><path d="M9 3v15M15 6v15"/></svg></div>

  <div class="abs photo" role="img" aria-label="Interior photo of the Verdaleaf Carousel cafe" style="left:24px;top:298px;width:130px;height:88px;background:linear-gradient(135deg,#6b3a22,#2a1a12)"></div>
  <div class="abs" style="left:24px;top:340px;background:var(--green);color:var(--white);font-size:8px;font-weight:800;padding:2px 8px;border-radius:0 8px 8px 0">90 points</div>
  <div class="abs" style="left:30px;top:372px;font-size:7.5px;font-weight:800;color:var(--white)">Verdaleaf Carousel</div>
  <div class="abs small" style="left:168px;top:304px;font-size:8.5px;line-height:2.3">
    <div>◷&nbsp; 5 mins away</div><div>⌾&nbsp; 1.45 Km</div><div style="line-height:1.2;padding-left:14px">Hours:<br>Opens soon&nbsp;&nbsp;&nbsp;9AM</div>
  </div>

  <div class="abs photo" role="img" aria-label="Interior photo of the Verdaleaf Waterfront Plaza cafe" style="left:24px;top:410px;width:130px;height:88px;background:linear-gradient(135deg,#1f5866,#15262e)"></div>
  <div class="abs" style="left:24px;top:452px;background:var(--green);color:var(--white);font-size:8px;font-weight:800;padding:2px 8px;border-radius:0 8px 8px 0">35 points</div>
  <div class="abs" style="left:30px;top:484px;font-size:7.5px;font-weight:800;color:var(--white)">Verdaleaf Waterfront Plaza</div>
  <div class="abs small" style="left:168px;top:416px;font-size:8.5px;line-height:2.3">
    <div>◷&nbsp; 5 mins away</div><div>⌾&nbsp; 1.45 Km</div><div style="line-height:1.2;padding-left:14px">Hours:<br>Opens soon&nbsp;&nbsp;&nbsp;9AM</div>
  </div>

  <div class="abs photo" role="img" aria-label="Interior photo of a third cafe" style="left:24px;top:522px;width:130px;height:70px;background:linear-gradient(135deg,#c9ccd0,#e6e8ea);opacity:.6"></div>
  <div class="abs small" style="left:168px;top:528px;font-size:8.5px;line-height:2.3;opacity:.3"><div>◷&nbsp; 5 mins away</div><div>⌾&nbsp; 1.45 Km</div></div>

  <nav class="nav">
    <span class="active"><svg viewBox="0 0 24 24"><path d="M3 11l9-7 9 7v10H3z"/><path d="M10 21v-6h4v6"/></svg></span>
    <span><svg viewBox="0 0 24 24"><path d="M3 3h8l10 10-8 8L3 11z"/><circle cx="8" cy="8" r="1.5"/></svg></span>
    <span><svg viewBox="0 0 24 24"><path d="M13 2L4 14h7l-1 8 9-12h-7z"/></svg></span>
    <span><svg viewBox="0 0 24 24"><rect x="2" y="5" width="20" height="14" rx="2"/><path d="M2 10h20"/></svg></span>
    <span><svg viewBox="0 0 24 24"><circle cx="12" cy="8" r="4"/><path d="M4 21c1-4 4-6 8-6s7 2 8 6"/></svg></span>
  </nav>
</section>

<!-- Menu list -->
<section class="screen" style="left:50px;top:1206px" aria-label="Menu items screen">
  <div class="abs" style="left:0;right:0;top:0;height:130px;background:var(--green)"></div>
  <svg class="abs" style="left:24px;top:52px" width="22" height="14" viewBox="0 0 22 14" fill="none" stroke="#fff" stroke-width="1.6" stroke-linecap="round"><path d="M21 7H2M7 1L1 7l6 6"/></svg>
  <div class="abs" style="left:0;right:0;top:50px;text-align:center;color:var(--white);font-size:12px;font-weight:800">Tasty items</div>
  <div class="abs avatar" role="img" aria-label="User profile photo" style="left:276px;top:42px;width:34px;height:34px"></div>
  <div class="abs" style="left:0;right:0;top:118px;bottom:0;background:var(--screen)"></div>
  <div class="round" style="left:276px;top:136px;width:24px;height:24px;background:var(--lime-pale)"><svg width="14" height="14" viewBox="0 0 24 24" fill="none" stroke="var(--green)" stroke-width="2"><path d="M2 3h3l3 12h11l2-8H6"/><circle cx="9" cy="20" r="1.5"/><circle cx="18" cy="20" r="1.5"/></svg></div>
  <span class="abs" style="left:294px;top:133px;width:7px;height:7px;border-radius:50%;background:var(--red)"></span>

  <div class="abs" style="left:0;top:130px;width:30px;height:130px;background:var(--lime)"></div>
  <div class="abs" style="left:0;top:260px;width:30px;height:130px;background:var(--green-mid)"></div>
  <div class="abs" style="left:0;top:390px;width:30px;bottom:0;background:var(--green-dark)"></div>
  <div class="side-label" style="top:250px;color:var(--green-dark)">Relish Fresh Tea</div>
  <div class="side-label" style="top:380px;color:var(--white)">Relish Fresh Tea</div>
  <div class="side-label" style="top:510px;color:var(--white)">Relish Fresh Tea</div>

  <div class="abs" style="left:76px;top:176px;width:62px;height:88px;border-radius:0 62px 0 0;background:var(--lime-pale)"></div>
  <div class="abs" style="left:156px;top:176px;width:62px;height:88px;border-radius:0 62px 0 0;background:var(--lime-pale)"></div>
  <div class="abs product-photo" role="img" aria-label="Product photo: jasmine green tea" style="left:66px;top:150px;width:26px;height:70px;background:#cfd6b0"></div>
  <div class="abs product-photo" role="img" aria-label="Product photo: mint tea" style="left:146px;top:150px;width:26px;height:70px;background:#8fd9cd"></div>
  <div class="abs product-photo" role="img" aria-label="Product photo: matcha tea" style="left:226px;top:150px;width:20px;height:70px;background:#dfe3cf"></div>
  <div class="abs meta" style="left:70px;top:270px;color:var(--ink)">Supreme Jasmine<br>Green Tea</div>
  <div class="abs meta" style="left:150px;top:270px;color:var(--ink)">Supreme Jasmine<br>Green Tea</div>

  <div class="abs" style="left:76px;top:316px;width:62px;height:90px;border-radius:0 62px 0 0;background:var(--green-mid)"></div>
  <div class="abs" style="left:156px;top:316px;width:62px;height:90px;border-radius:0 62px 0 0;background:var(--green-mid)"></div>
  <div class="abs product-photo" role="img" aria-label="Product photo: mango tea" style="left:66px;top:290px;width:26px;height:72px;background:#f6b84a"></div>
  <div class="abs product-photo" role="img" aria-label="Product photo: strawberry tea" style="left:146px;top:290px;width:26px;height:72px;background:#f28890"></div>
  <div class="abs product-photo" role="img" aria-label="Product photo: taro tea" style="left:226px;top:290px;width:20px;height:72px;background:#dcccf0"></div>
  <div class="abs meta" style="left:70px;top:412px;color:var(--ink)">Supreme Jasmine<br>Green Tea</div>
  <div class="abs meta" style="left:150px;top:412px;color:var(--ink)">Supreme Jasmine<br>Green Tea</div>

  <div class="abs" style="left:76px;top:462px;width:62px;height:80px;border-radius:0 62px 0 0;background:var(--green-dark)"></div>
  <div class="abs" style="left:156px;top:462px;width:62px;height:80px;border-radius:0 62px 0 0;background:var(--green-dark)"></div>
  <div class="abs product-photo" role="img" aria-label="Product photo: lemon tea" style="left:66px;top:440px;width:26px;height:64px;background:#ecd040"></div>
  <div class="abs product-photo" role="img" aria-label="Product photo: dragon fruit tea" style="left:146px;top:440px;width:26px;height:64px;background:#ee78c0"></div>
  <div class="abs product-photo" role="img" aria-label="Product photo: peach tea" style="left:226px;top:440px;width:20px;height:64px;background:#f6b8b8"></div>

  <nav class="nav">
    <span class="active"><svg viewBox="0 0 24 24"><path d="M3 11l9-7 9 7v10H3z"/><path d="M10 21v-6h4v6"/></svg></span>
    <span><svg viewBox="0 0 24 24"><path d="M3 3h8l10 10-8 8L3 11z"/><circle cx="8" cy="8" r="1.5"/></svg></span>
    <span><svg viewBox="0 0 24 24"><path d="M13 2L4 14h7l-1 8 9-12h-7z"/></svg></span>
    <span><svg viewBox="0 0 24 24"><rect x="2" y="5" width="20" height="14" rx="2"/><path d="M2 10h20"/></svg></span>
    <span><svg viewBox="0 0 24 24"><circle cx="12" cy="8" r="4"/><path d="M4 21c1-4 4-6 8-6s7 2 8 6"/></svg></span>
  </nav>
</section>

<!-- Product detail -->
<section class="screen" style="left:430px;top:1206px" aria-label="Product detail screen">
  <div class="abs" style="left:0;right:0;top:0;height:530px;background:var(--green-mid);border-radius:0 0 40px 0"></div>
  <div class="abs" style="left:0;right:0;top:0;height:410px;background:var(--lime);border-radius:0 0 40px 0"></div>
  <div class="abs" style="left:0;right:0;top:0;height:300px;background:var(--green);border-radius:0 0 40px 0"></div>
  <svg class="abs" style="left:22px;top:52px" width="22" height="14" viewBox="0 0 22 14" fill="none" stroke="#fff" stroke-width="1.6" stroke-linecap="round"><path d="M21 7H2M7 1L1 7l6 6"/></svg>
  <div class="round" style="left:284px;top:42px;width:26px;height:26px;background:rgba(255,255,255,.35)"><svg width="14" height="14" viewBox="0 0 24 24" fill="none" stroke="#fff" stroke-width="2"><path d="M12 21s-8-5-8-11a4 4 0 018-1 4 4 0 018 1c0 6-8 11-8 11z"/></svg></div>
  <div class="abs product-photo" role="img" aria-label="Product photo: Supreme Jasmine Green Tea" style="left:124px;top:52px;width:72px;height:160px;background:linear-gradient(#bfe08a,#8fc85a)"></div>
  <div class="abs" style="left:26px;top:234px;color:var(--white);font-size:14px;font-weight:800;line-height:1.15">Supreme Jasmine<br>Green Tea</div>
  <div class="abs" style="left:26px;top:270px;color:var(--white);font-size:8px">★ ★ ★ ★ ★ &nbsp;(90 reviews)</div>
  <div class="abs" style="left:224px;top:228px;width:76px;height:52px;background:var(--green-dark);border-radius:0 0 0 20px;color:var(--white);padding:10px 10px">
    <span style="font-size:8px;vertical-align:top">$</span><span style="font-size:18px;font-weight:700"> 4.50</span>
  </div>
  <div class="abs" style="left:26px;top:316px;font-size:12px;font-weight:800;color:var(--green-dark)">Choose Size</div>
  <div class="abs option-box" style="left:70px;top:340px;width:30px;height:34px;background:var(--green)"></div>
  <div class="abs meta" style="left:64px;top:380px;color:var(--ink)">Medium</div>
  <div class="abs option-box" style="left:190px;top:332px;width:34px;height:42px;background:var(--white)"></div>
  <div class="abs meta" style="left:196px;top:380px;color:var(--ink)">Large</div>
  <div class="abs meta" style="left:232px;top:348px;color:#e18b3c">(+$0.50)</div>
  <div class="abs" style="left:26px;top:428px;font-size:12px;font-weight:800;color:var(--green-dark)">Sweetness</div>
  <div class="abs" style="left:26px;top:456px;width:270px;display:flex;justify-content:space-between">
    <div style="text-align:center"><div class="option-box" style="width:26px;height:30px;background:var(--white);margin:0 auto"></div><div class="small" style="color:var(--white);margin-top:4px">25%</div></div>
    <div style="text-align:center"><div class="option-box" style="width:26px;height:30px;background:var(--white);margin:0 auto"></div><div class="small" style="color:var(--white);margin-top:4px">50%</div></div>
    <div style="text-align:center"><div class="option-box" style="width:26px;height:30px;background:var(--green);margin:0 auto"></div><div class="small" style="color:var(--white);margin-top:4px">75%</div></div>
    <div style="text-align:center"><div class="option-box" style="width:26px;height:30px;background:var(--white);margin:0 auto"></div><div class="small" style="color:var(--white);margin-top:4px">100%</div></div>
  </div>
  <div class="abs" style="left:26px;top:544px;font-size:11px;font-weight:800;color:var(--green-dark)">Ice</div>
  <div class="abs" style="left:26px;top:564px;white-space:nowrap"><span class="chip on">Full</span><span class="chip">Less</span><span class="chip">No ice</span><span class="chip">Warm</span></div>
  <div class="round" style="left:268px;top:584px;width:44px;height:44px;background:var(--green);box-shadow:0 6px 14px rgba(47,138,42,.35)"><svg width="20" height="20" viewBox="0 0 24 24" fill="none" stroke="#fff" stroke-width="2"><path d="M2 3h3l3 12h11l2-8H6"/><circle cx="9" cy="20" r="1.5"/><circle cx="18" cy="20" r="1.5"/></svg></div>
  <nav class="nav">
    <span class="active"><svg viewBox="0 0 24 24"><path d="M3 11l9-7 9 7v10H3z"/><path d="M10 21v-6h4v6"/></svg></span>
    <span><svg viewBox="0 0 24 24"><path d="M3 3h8l10 10-8 8L3 11z"/><circle cx="8" cy="8" r="1.5"/></svg></span>
    <span><svg viewBox="0 0 24 24"><path d="M13 2L4 14h7l-1 8 9-12h-7z"/></svg></span>
    <span><svg viewBox="0 0 24 24"><rect x="2" y="5" width="20" height="14" rx="2"/><path d="M2 10h20"/></svg></span>
    <span><svg viewBox="0 0 24 24"><circle cx="12" cy="8" r="4"/><path d="M4 21c1-4 4-6 8-6s7 2 8 6"/></svg></span>
  </nav>
</section>

<!-- Checkout -->
<section class="screen" style="left:810px;top:1206px;background:var(--green)" aria-label="Checkout screen">
  <svg class="abs" style="left:24px;top:52px" width="22" height="14" viewBox="0 0 22 14" fill="none" stroke="#fff" stroke-width="1.6" stroke-linecap="round"><path d="M21 7H2M7 1L1 7l6 6"/></svg>
  <div class="abs" style="left:0;right:0;top:50px;text-align:center;color:var(--white);font-size:12px;font-weight:800">Checkout</div>

  <div class="abs" style="left:22px;right:22px;top:96px;height:80px;background:var(--white);border-radius:40px"></div>
  <div class="abs product-photo" role="img" aria-label="Product photo: Supreme Jasmine Green Tea" style="left:26px;top:84px;width:32px;height:76px;background:#cfd6b0"></div>
  <div class="abs" style="left:82px;top:108px;font-size:10px;font-weight:700">Supreme Jasmine Green Tea</div>
  <div class="abs meta" style="left:82px;top:126px">Size :<br>Sweetness :<br>Ice :</div>
  <div class="abs meta" style="left:150px;top:126px">Medium<br>75%<br>No ice</div>
  <div class="abs" style="left:256px;top:124px;font-size:14px;font-weight:600;color:var(--green)">$4.50</div>
  <div class="round" style="left:160px;top:166px;width:20px;height:20px;background:var(--red);font-size:12px">×</div>
  <div class="round" style="left:190px;top:166px;width:20px;height:20px;background:var(--gold)"></div>
  <div class="round" style="left:220px;top:166px;width:20px;height:20px;background:var(--green);border:2px solid var(--white);font-size:12px">+</div>

  <div class="abs" style="left:22px;right:22px;top:206px;height:80px;background:var(--white);border-radius:40px"></div>
  <div class="abs product-photo" role="img" aria-label="Product photo: mango tea" style="left:26px;top:194px;width:32px;height:76px;background:#f6b84a"></div>
  <div class="abs" style="left:82px;top:218px;font-size:10px;font-weight:700">Supreme Jasmine Green Tea</div>
  <div class="abs meta" style="left:82px;top:236px">Size :<br>Sweetness :<br>Ice :</div>
  <div class="abs meta" style="left:150px;top:236px">Medium<br>75%<br>No ice</div>
  <div class="abs" style="left:256px;top:234px;font-size:14px;font-weight:600;color:var(--green)">$4.50</div>
  <div class="round" style="left:160px;top:276px;width:20px;height:20px;background:var(--red);font-size:12px">×</div>
  <div class="round" style="left:190px;top:276px;width:20px;height:20px;background:var(--gold)"></div>
  <div class="round" style="left:220px;top:276px;width:20px;height:20px;background:var(--green);border:2px solid var(--white);font-size:12px">+</div>

  <div class="abs" style="left:40px;top:336px;color:var(--white);font-size:9px;font-weight:700;line-height:1.2">Enter your<br>coupon code</div>
  <div class="abs" style="left:130px;top:358px;width:100px;height:1px;background:rgba(255,255,255,.7)"></div>
  <div class="round" style="left:248px;top:332px;width:26px;height:26px;background:var(--white)"><svg width="12" height="12" viewBox="0 0 24 24" fill="none" stroke="var(--ink)" stroke-width="3"><path d="M4 12l5 5L20 6"/></svg></div>

  <div class="abs" style="left:18px;right:0;top:404px;bottom:0;background:var(--white);border-radius:50px 0 0 0"></div>
  <div class="abs" style="left:42px;top:422px;font-size:10px;font-weight:800;color:var(--green)">Your Favorite</div>
  <div class="abs product-photo" role="img" aria-label="Product photo: lemon tea" style="left:48px;top:450px;width:26px;height:62px;background:#ecd040"></div>
  <div class="abs product-photo" role="img" aria-label="Product photo: strawberry tea" style="left:118px;top:450px;width:26px;height:62px;background:#f28890"></div>
  <div class="abs product-photo" role="img" aria-label="Product photo: green tea" style="left:188px;top:450px;width:26px;height:62px;background:#c6d65a"></div>
  <div class="abs product-photo" role="img" aria-label="Product photo: mango tea" style="left:256px;top:450px;width:22px;height:62px;background:#f6b84a"></div>
  <div class="round" style="left:64px;top:496px;width:20px;height:20px;background:var(--green);border:2px solid var(--white);font-size:12px">+</div>
  <div class="round" style="left:134px;top:496px;width:20px;height:20px;background:var(--green);border:2px solid var(--white);font-size:12px">+</div>
  <div class="round" style="left:204px;top:496px;width:20px;height:20px;background:var(--green);border:2px solid var(--white);font-size:12px">+</div>

  <div class="abs" style="left:44px;top:558px;font-size:7px;font-weight:600">Wallet<div style="font-size:10px;font-weight:800">$250.55</div></div>
  <div class="abs" style="left:116px;top:558px;font-size:7px;font-weight:600">Points<div style="font-size:10px;font-weight:800">1522</div></div>
  <div class="abs" style="left:234px;top:562px;font-size:15px;font-weight:700;color:var(--green)">$19.95</div>

  <div class="abs" style="left:40px;right:26px;top:612px;height:34px;border-radius:17px;background:var(--white);box-shadow:0 6px 16px rgba(80,90,110,.14);overflow:hidden;display:flex">
    <div style="flex:1;display:flex;align-items:center;gap:10px;padding-left:14px;color:var(--green);font-size:10px;font-weight:700"><svg width="14" height="14" viewBox="0 0 24 24" fill="none" stroke="var(--green)" stroke-width="2"><path d="M2 3h3l3 12h11l2-8H6"/><circle cx="9" cy="20" r="1.5"/><circle cx="18" cy="20" r="1.5"/></svg>3 items</div>
    <div style="width:88px;background:var(--green);color:var(--white);display:flex;align-items:center;justify-content:center;gap:8px;font-size:10px;font-weight:700">Continue <svg width="16" height="10" viewBox="0 0 22 14" fill="none" stroke="#fff" stroke-width="1.8" stroke-linecap="round"><path d="M1 7h19M15 1l6 6-6 6"/></svg></div>
  </div>
</section>

</div>
</body>
</html>
```